I need a Billboard Design for our company called hoverQUEST.
I'm completely open for any design idea, but it must be professional and adventurous. The Billboard is 10ft high and 20ft wide.
Our Slogan is: "The ULTIMATE HELICOPTER DOORS-OFF Experience."
"Say YES to New Adventures"
Locations: SARASOTA | TAMPA | NAPLES
Prices Starting at $99.
Hotline: (855) HOV-QUES(t) (855) 468-7837
www.hoverQUEST.example
Target Market(s)
Aviation, Tourism
Industry/Entity Type
Tourism
Requirements
Must have
- The Design should match our website design at www.hoverQUEST.example
Please checkout the website for ideas. Thank you

```html
<!DOCTYPE html>
<html lang="en">
<head>
<meta charset="utf-8">
<title>hoverQUEST Billboard</title>
<link rel="stylesheet" href="https://fonts.googleapis.com/css2?family=Arimo:wght@400;700&family=Montserrat:wght@700&family=Roboto+Condensed:wght@400;700&display=swap">
<style>
  :root {
    --brand-blue: #1f36a5;
    --accent-blue: #9dbde8;
    --logo-blue: #3f73b8;
    --white: #ffffff;
    --stage: #e9eef4;
    --sky-light: #eef2f5;
    --city-mid: #a9bccb;
    --city-deep: #6f8ea6;
    --cabin-light: #d9cfc6;
    --cabin-deep: #8a7d74;
  }
  * { margin: 0; padding: 0; box-sizing: border-box; }
  html, body { width: 1200px; height: 892px; overflow: hidden; background: var(--stage); }
  .billboard {
    position: absolute; left: 0; top: 176px;
    width: 1200px; height: 540px; overflow: hidden;
    font-family: "Arimo", Arial, sans-serif; color: var(--white);
  }
  .billboard svg.backdrop { position: absolute; inset: 0; }
  .brand-name {
    position: absolute; left: 57px; top: 70px;
    font-size: 26px; font-weight: 700; color: var(--logo-blue);
    display: flex; align-items: center; gap: 10px;
  }
  .brand-name .dot { width: 14px; height: 14px; border-radius: 50%; background: var(--logo-blue); }
  .headline { position: absolute; left: 355px; top: 94px; line-height: 1; }
  .headline .line-one { font-size: 24px; letter-spacing: 0.5px; }
  .headline .line-two { margin-top: 6px; padding-left: 16px; font-size: 19px; }
  .headline .line-two strong { font-size: 31px; font-weight: 700; color: var(--accent-blue); margin-left: 2px; }
  .tagline { position: absolute; left: 257px; top: 212px; line-height: 1; }
  .tagline .say { padding-left: 12px; font-size: 19px; }
  .tagline .say strong { font-size: 32px; color: var(--accent-blue); }
  .tagline .adventures { margin-top: 6px; font-family: "Montserrat", Arial, sans-serif; font-size: 32px; font-weight: 700; }
  .contact { position: absolute; left: 110px; top: 393px; font-weight: 700; }
  .contact .hotline { font-size: 18px; }
  .contact .number { font-size: 27px; margin-top: 4px; }
  .contact .rule { width: 280px; height: 2px; background: var(--white); margin: 8px 0 0 -17px; }
  .contact .web { font-size: 17px; margin-top: 10px; }
  .contact .cities { font-size: 15px; margin-top: 12px; letter-spacing: 0.6px; }
  .price-badge {
    position: absolute; left: 684px; top: 349px; width: 166px; height: 166px;
    border-radius: 50%; background: var(--brand-blue); border: 4px solid var(--white);
    display: flex; flex-direction: column; align-items: center; justify-content: center;
    font-family: "Roboto Condensed", Arial, sans-serif; text-align: center; line-height: 1.15;
  }
  .price-badge .label { font-size: 20px; }
  .price-badge .amount { font-size: 46px; font-weight: 700; line-height: 1.1; }
</style>
</head>
<body>
<main class="billboard">
  <svg class="backdrop" width="1200" height="540" viewBox="0 0 1200 540">
    <defs>
      <linearGradient id="cityTone" x1="0" y1="0" x2="0" y2="1">
        <stop offset="0" stop-color="var(--sky-light)"/>
        <stop offset="0.45" stop-color="var(--city-mid)"/>
        <stop offset="1" stop-color="var(--city-deep)"/>
      </linearGradient>
      <linearGradient id="leftFade" x1="0" y1="0" x2="1" y2="0">
        <stop offset="0" stop-color="#ffffff" stop-opacity="0.85"/>
        <stop offset="1" stop-color="#ffffff" stop-opacity="0"/>
      </linearGradient>
      <linearGradient id="cabinTone" x1="0" y1="0" x2="1" y2="1">
        <stop offset="0" stop-color="var(--cabin-light)"/>
        <stop offset="1" stop-color="var(--cabin-deep)"/>
      </linearGradient>
    </defs>
    <rect class="aerial-photo" width="1200" height="540" fill="url(#cityTone)" role="img" aria-label="Aerial photo of a coastal city seen from a helicopter"/>
    <rect class="aerial-fade" width="500" height="540" fill="url(#leftFade)"/>
    <polygon class="passenger-photo" points="960,0 1200,0 1200,540 824,540 824,90" fill="url(#cabinTone)" role="img" aria-label="Photo of a passenger with headset looking out of an open helicopter door"/>
    <polygon class="diagonal-band" points="410,0 914,0 437,540 0,540 0,464" fill="var(--brand-blue)"/>
  </svg>

  <div class="brand-name"><span class="dot"></span>hoverQUEST</div>

  <div class="headline">
    <div class="line-one">THE ULTIMATE HELICOPTER</div>
    <div class="line-two">DOORS-OFF <strong>EXPERIENCE</strong></div>
  </div>

  <div class="tagline">
    <div class="say">SAY <strong>YES</strong> TO NEW</div>
    <div class="adventures">ADVENTURES</div>
  </div>

  <div class="contact">
    <div class="hotline">Hotline: (855) HOV-QUES(t)</div>
    <div class="number">(855) 468-7837</div>
    <div class="rule"></div>
    <div class="web">www.hoverQUEST.example</div>
    <div class="cities">SARASOTA | TAMPA | NAPLES</div>
  </div>

  <div class="price-badge">
    <span class="label">Prices</span>
    <span class="label">Starting at</span>
    <span class="amount">$99</span>
  </div>
</main>
</body>
</html>
```